Cleaning Company needs a new business card design

Hi, We are looking for new business card designs to update with our latest logo and company information.
We would like to see designs using the colours:
Royal Blue #4169E1 - this is our company colour so this has to be in there. Please feel free to experiment with other colours.
Must include:
Front of business card:
Logo
Back of the business card:
0800 519 2867
07946 581 302
Email: info@pelvormaids.co.uk
Web: www.pelvormaids.co.uk
Services:
End of Tenancy
Carpet & Upholstery
Regular & One Off
all work fully insured.
The front of the business card with the logo can be made to look raised print. The blue man to be a shiny finish.
The business card needs to be presented in a matt finish
The business must be in the following styles:
Standard Square with rounded corners.
Thank you to all that take part in this.
Target Market(s)
Men and Women of different ages in the UK.
Industry/Entity Type
House Cleaning
Contact Information for Business Card
Front of business card:
Logo
0800 519 2867
07946 581 302
Email: pelvormaids@brimmail.co.uk
Services:
End of Tenancy
Carpet & Upholstery
Regular & One Off
all work fully insured.

```html
<!DOCTYPE html>
<html lang="en">
<head>
<meta charset="utf-8">
<title>Pelvor Maids – Business Card</title>
<link href="https://fonts.googleapis.com/css2?family=Questrial&display=swap" rel="stylesheet">
<style>
  :root {
    --page-bg: #2a2a2c;
    --card-bg: #1b1b1d;
    --royal-blue: #4169E1;
    --sky-blue: #1fa8e3;
    --text-light: #e6e6e8;
    --divider: #55565a;
  }
  html, body {
    margin: 0;
    padding: 0;
    width: 1200px;
    height: 900px;
    overflow: hidden;
    background: var(--page-bg);
    font-family: "Questrial", "Century Gothic", sans-serif;
  }
  .canvas {
    position: relative;
    width: 1200px;
    height: 900px;
  }
  .card {
    position: absolute;
    top: 282px;
    width: 520px;
    height: 336px;
    background: var(--card-bg);
    border-radius: 22px;
    overflow: hidden;
  }
  .card--front { left: 60px; }
  .card--back { left: 620px; }

  /* Front */
  .brand {
    position: absolute;
    inset: 0;
    display: flex;
    align-items: center;
    justify-content: center;
  }
  .brand__name {
    font-size: 48px;
    color: var(--royal-blue);
    letter-spacing: 0.5px;
  }

  /* Back */
  .figure-area {
    position: absolute;
    left: 62px;
    top: 62px;
    width: 150px;
    height: 212px;
    border-radius: 14px;
    background: linear-gradient(160deg, #27b2ec, #1794cc);
  }
  .divider {
    position: absolute;
    left: 262px;
    top: 34px;
    width: 1px;
    height: 268px;
    background: var(--divider);
  }
  .details {
    position: absolute;
    left: 282px;
    top: 40px;
    right: 20px;
    color: var(--text-light);
  }
  .details__name {
    margin: 0;
    font-size: 22px;
    font-weight: 400;
    color: var(--sky-blue);
  }
  .details__role {
    margin: 4px 0 18px;
    font-size: 14px;
    color: var(--sky-blue);
  }
  .contact-list, .service-list {
    list-style: none;
    margin: 0;
    padding: 0;
  }
  .contact-list li {
    display: flex;
    align-items: center;
    gap: 8px;
    font-size: 12.5px;
    line-height: 21px;
  }
  .contact-list svg {
    width: 12px;
    height: 12px;
    flex: none;
    fill: var(--royal-blue);
  }
  .service-list {
    margin-top: 18px;
  }
  .service-list li {
    position: relative;
    padding-left: 16px;
    font-size: 13px;
    line-height: 22px;
  }
  .service-list li::before {
    content: "";
    position: absolute;
    left: 2px;
    top: 9px;
    width: 5px;
    height: 5px;
    border-radius: 50%;
    background: var(--royal-blue);
  }
</style>
</head>
<body>
<main class="canvas">
  <section class="card card--front" aria-label="Card front">
    <div class="brand">
      <span class="brand__name">Pelvor Maids</span>
    </div>
  </section>

  <section class="card card--back" aria-label="Card back">
    <div class="figure-area" role="img" aria-label="Blue figure of a person vacuuming"></div>
    <div class="divider"></div>
    <div class="details">
      <h1 class="details__name">Daniel Harrow</h1>
      <p class="details__role">CEO/Founder</p>
      <ul class="contact-list">
        <li>
          <svg viewBox="0 0 24 24" aria-hidden="true"><path d="M6.6 10.8a15.1 15.1 0 0 0 6.6 6.6l2.2-2.2a1 1 0 0 1 1-.25 11.4 11.4 0 0 0 3.6.57 1 1 0 0 1 1 1V20a1 1 0 0 1-1 1A17 17 0 0 1 3 4a1 1 0 0 1 1-1h3.5a1 1 0 0 1 1 1c0 1.25.2 2.45.57 3.57a1 1 0 0 1-.25 1z"/></svg>
          0800 519 2867
        </li>
        <li>
          <svg viewBox="0 0 24 24" aria-hidden="true"><path d="M7 1h10a2 2 0 0 1 2 2v18a2 2 0 0 1-2 2H7a2 2 0 0 1-2-2V3a2 2 0 0 1 2-2zm0 3v14h10V4z"/></svg>
          07946 581 302
        </li>
        <li>
          <svg viewBox="0 0 24 24" aria-hidden="true"><path d="M2 5h20v14H2zm2 2v.5l8 5 8-5V7z"/></svg>
          pelvormaids@brimmail.co.uk
        </li>
        <li>
          <svg viewBox="0 0 24 24" aria-hidden="true"><path d="M12 2a10 10 0 1 0 0 20 10 10 0 0 0 0-20zm0 2c.9 1.2 1.6 2.6 2 4h-4c.4-1.4 1.1-2.8 2-4zM4.3 14a8 8 0 0 1 0-4h3.4a16 16 0 0 0 0 4zm5.7 0a14 14 0 0 1 0-4h4a14 14 0 0 1 0 4zm6.3 0a16 16 0 0 0 0-4h3.4a8 8 0 0 1 0 4zM12 20c-.9-1.2-1.6-2.6-2-4h4c-.4 1.4-1.1 2.8-2 4z"/></svg>
          www.pelvormaids.co.uk
        </li>
      </ul>
      <ul class="service-list">
        <li>End of Tenancy</li>
        <li>Carpet &amp; Upholstery</li>
        <li>Regular &amp; One Off</li>
        <li>all work fully insured</li>
      </ul>
    </div>
  </section>
</main>
</body>
</html>
```